I need a business Card Design for my practice , i am clinical herbalist. I am a herbalist specializing in Lyme disease, autism, autoimmune diseases, difficult to cure diseasesDifficult to cure diseases. In my innovative practice i link traditional medicine, herbs with science, immunologu ,pharmacology.

Industry/Entity Type

Business

Contact Information for Business Card

My company name : OŚRODEK ZIELNIK
My name : Piotr Kaleta
Name of my profession : Fitoterapeuta
In Polish language Fitoterapeuta is Herbalist .

e-mail: piotrkaleta@osrodekzielnik.com
www.osrodek-zielnik.pl
phone : 604 587 231
My company adress : Dąbrowa Sitnicka 41 , 38-415 Lużna
I dont have logo .

Requirements
Nice to have
• My company

```html
<!DOCTYPE html>
<html lang="pl">
<head>
<meta charset="utf-8">
<title>Ośrodek Zielnik – wizytówka</title>
<link href="https://fonts.googleapis.com/css2?family=Fira+Sans+Condensed:wght@700&family=Libre+Baskerville:wght@400&display=swap" rel="stylesheet">
<style>
  :root {
    --herb-green: #137c3e;
    --herb-pale: #d9ebe0;
    --herb-mid: #9cc9ad;
    --paper: #ffffff;
    --rule: #b9ad8c;
    --ink-light: #ffffff;
  }
  html, body {
    margin: 0;
    padding: 0;
    width: 1200px;
    height: 900px;
    overflow: hidden;
    background: var(--paper);
  }
  .business-card {
    position: absolute;
    left: 211px;
    top: 203px;
    width: 792px;
    height: 513px;
    box-sizing: border-box;
    border: 1px solid var(--herb-green);
    background: var(--paper);
    overflow: hidden;
  }
  .green-panel {
    position: absolute;
    left: 320px;
    top: 0;
    right: 0;
    bottom: 0;
    background: var(--herb-green);
  }
  .plant-illustration {
    position: absolute;
    left: 232px;
    top: 0;
    width: 180px;
    height: 513px;
    background:
      radial-gradient(ellipse 60% 35% at 40% 22%, var(--herb-mid) 0%, transparent 70%),
      radial-gradient(ellipse 55% 30% at 55% 65%, var(--herb-mid) 0%, transparent 70%),
      linear-gradient(180deg, var(--herb-pale) 0%, #bcdcc8 50%, var(--herb-pale) 100%);
  }
  .card-text {
    position: absolute;
    right: 22px;
    text-align: right;
    color: var(--ink-light);
    margin: 0;
    white-space: nowrap;
  }
  .company-name {
    top: 16px;
    font-family: "Fira Sans Condensed", "Arial Narrow", sans-serif;
    font-weight: 700;
    font-size: 42px;
    line-height: 48px;
    letter-spacing: 0.5px;
  }
  .company-rule {
    position: absolute;
    left: 349px;
    right: 22px;
    top: 62px;
    height: 1px;
    background: var(--rule);
  }
  .person-name {
    top: 80px;
    font-family: "Libre Baskerville", "Century Schoolbook", serif;
    font-size: 33px;
    line-height: 46px;
    font-weight: 400;
  }
  .profession {
    top: 126px;
    font-family: "Libre Baskerville", "Century Schoolbook", serif;
    font-size: 19px;
    line-height: 30px;
  }
  .contact-list {
    bottom: 2px;
    font-family: "Libre Baskerville", "Century Schoolbook", serif;
    font-size: 17.5px;
    line-height: 27.5px;
    list-style: none;
    padding: 0;
  }
</style>
</head>
<body>
  <div class="business-card">
    <div class="green-panel"></div>
    <div class="plant-illustration" role="img" aria-label="Rysunek kwitnącej rośliny zielarskiej (babka) z kłosami i liśćmi, w bieli i zieleni"></div>

    <h1 class="card-text company-name">OŚRODEK ZIELNIK</h1>
    <div class="company-rule"></div>
    <p class="card-text person-name">Piotr Kaleta</p>
    <p class="card-text profession">Fitoterapeuta</p>

    <ul class="card-text contact-list">
      <li>piotrkaleta@osrodekzielnik.com</li>
      <li>www.osrodek-zielnik.pl</li>
      <li>604 587 231</li>
      <li>Dąbrowa Sitnicka 41 , 38-415 Lużna</li>
    </ul>
  </div>
</body>
</html>
```